依頼詳細
【背景】
弊社は平成17年の創業以来、パチンコ店の広告物を主に企画提案〜制作、折込などの代理店業を行ってきました。
しかし、パチンコ業界の規制強化などの理由から、パチンコ業界以外の業種の広告物やBtoBの販促企画•制作、また最近では農家のブランディングなどの仕事にシフトしてきています。
そのような状況の中、弊社の代表自らもMBAのビジネススクールに通いマーケティング等を学び直しており、今後は現状の制作メインの仕事だけではなく、さらに川上のマーケティングや広告戦略といった、もっとクライアントに入り込んだお手伝いが出来る力をつけていきたいと考えています。
その為には再度、組織の再構築、強みを活かせる組織づくりを行っていく必要があり、設立10年を前に第二創業といった心づもりで企業理念を変更しようと考えています。
また、企業理念はこの会社は何の為に存在しているのかを言語化したものであり、在職中のスタッフだけではなく、今後採用予定の方にも共感した上で働いていただきたいと考えています。

【仕様】
・A3縦で制作してください
・納品はイラレデータでお願いします
・イメージは実際の経営理念から想像してください
記載項目
企業理念

Creative Happy!
-社会のHappy!
-顧客のHappy!
-仲間のHappy!
-家族のHappy!
-自分のHappy!

会社ロゴ

【解説(ココは記載不要です)】
Creative Happy! … 広告物を作るのではなく、その先にあるHappyを作っているという意識。
例えば、ケーキ屋さんのDMを作る際、「ケーキ屋さんのDMをつくっている」という意識ではなく「家族で美味しそうにこのケーキを食べている姿」つまり「その先のHappy!」を意識・想像して作ることが出来れば、仕事の質に大きな差が生じると考えています。

-社会のHappy!
-顧客のHappy!
-仲間のHappy!
-家族のHappy!
-自分のHappy!
仕事をする上で「Happy!を考える順番」を意味しています。
希望イメージ
シンプル 複雑
単色 カラフル
暗い 明るい
日常 高級
遊び心 厳粛
未来的 伝統的
女性的 男性的
希望する色
納品ファイル
• イラストレーター形式 (.ai)
補足説明
■ 選んだ理由

まずイメージが明るくHAPPYな感じがしたこと
次に非常にわかりやすいビジュアルでストーリーを作ってくださったことが
kitazono-teさんのデザインを選んだ理由です。

■ 提案者全員のお礼・コメント

皆様にはご提案をいただき感謝いたします。
今回、大変多くの方からご提案をいただき、素敵なデザインが他にもあり社内でも選考するのに随分意見が出ました。

今回は弊社の社内的なポスターでしたが、弊社は広告代理業を行っているためチラシやDMなど他のグラフィックデザインも仕事として発生しています。(携帯電話のチラシなど)
またお願いすることもあるかと思いますので、どうぞよろしくお願いします。

```html
<!DOCTYPE html>
<html lang="ja">
<head>
<meta charset="utf-8">
<title>Creative Happy! 企業理念</title>
<link rel="stylesheet" href="https://fonts.googleapis.com/css2?family=Questrial&family=M+PLUS+1p:wght@500;800&display=swap">
<style>
  :root {
    --frame: #a89280;
    --frame-line: #8b7462;
    --paper: #ffffff;
    --ink: #3a3030;
    --pink: #e8428c;
    --orange: #f39a2b;
    --yellow: #f1d234;
    --green: #8cc63f;
    --sky: #4fb6e6;
    --blue: #5b7fd0;
    --purple: #9b6bc2;
    --mauve: #a98fb0;
    --rose: #f2a3bf;
    --mint: #9fd9b4;
    --lilac: #c5b3e0;
    --peach: #f8c08a;
    --grey: #cfc8c4;
    --ghost: rgba(255,255,255,0.55);
    --ornament: #f0b6a8;
  }
  * { margin: 0; padding: 0; box-sizing: border-box; }
  html, body { width: 848px; height: 1200px; overflow: hidden; background: var(--paper); }
  .poster {
    position: relative; width: 848px; height: 1200px;
    background: var(--frame); padding: 22px;
  }
  .sheet {
    position: relative; width: 100%; height: 100%;
    background: var(--paper);
    outline: 2px solid var(--frame-line); outline-offset: -8px;
  }
  .title {
    font-family: "Questrial", sans-serif; font-weight: 400; line-height: 1;
    position: absolute;
  }
  .title span { display: inline-block; }
  .title--creative { left: 78px; top: 80px; font-size: 108px; letter-spacing: -1px; }
  .title--happy { right: 58px; top: 186px; font-size: 112px; letter-spacing: -1px; }
  .swoosh { position: absolute; left: 110px; top: 140px; }
  .sparkle { position: absolute; border-radius: 50%; background: var(--ornament); }
  .values {
    position: absolute; left: 76px; top: 385px; list-style: none;
    display: flex; flex-direction: column; gap: 9px;
  }
  .value { display: flex; align-items: center; height: 66px; }
  .value__label {
    font-family: "M PLUS 1p", sans-serif; font-weight: 500;
    font-size: 50px; color: var(--ink); width: 192px; letter-spacing: 1px; line-height: 1;
  }
  .value__word { display: flex; gap: 5px; }
  .tile {
    width: 66px; height: 66px;
    display: flex; align-items: center; justify-content: center;
    font-family: "Questrial", sans-serif; font-size: 54px; color: var(--ghost);
    line-height: 1; padding-bottom: 6px;
  }
  .value__bang {
    font-family: "M PLUS 1p", sans-serif; font-weight: 800;
    font-size: 64px; margin-left: 10px; line-height: 1;
    transform: skewX(-10deg);
  }
  .brand {
    position: absolute; left: 0; right: 0; top: 950px; text-align: center;
    font-family: "M PLUS 1p", sans-serif; font-weight: 800;
    font-size: 66px; letter-spacing: 4px; color: var(--ink); line-height: 1;
  }
  .ornament { position: absolute; }
  .ornament--left {
    left: 14px; bottom: 14px; width: 200px; height: 150px;
    background: radial-gradient(circle at 30% 70%, #f3a996 0%, #f7cbbd 45%, rgba(255,255,255,0) 75%);
  }
  .ornament--right {
    right: 14px; bottom: 14px; width: 230px; height: 90px;
    background: linear-gradient(200deg, rgba(255,255,255,0) 10%, #ead9cf 60%, #dbbfaf 100%);
  }
</style>
</head>
<body>
<main class="poster">
  <div class="sheet">
    <h1 class="title title--creative" aria-label="Creative">
      <span style="color:var(--pink)">C</span><span style="color:var(--orange)">r</span><span style="color:var(--green)">e</span><span style="color:var(--sky)">a</span><span style="color:var(--purple)">t</span><span style="color:var(--pink)">i</span><span style="color:var(--blue)">v</span><span style="color:var(--green)">e</span>
    </h1>
    <svg class="swoosh" width="460" height="90" viewBox="0 0 460 90" aria-hidden="true">
      <path d="M10 60 Q200 95 450 20" fill="none" stroke="var(--orange)" stroke-width="2"/>
    </svg>
    <div class="sparkle" role="img" aria-label="small flower ornament" style="left:612px;top:60px;width:34px;height:34px;background:var(--yellow)"></div>
    <div class="sparkle" role="img" aria-label="small flower ornament" style="left:96px;top:196px;width:24px;height:24px"></div>
    <div class="sparkle" role="img" aria-label="small flower ornament" style="left:742px;top:322px;width:20px;height:20px;background:var(--rose)"></div>
    <p class="title title--happy" aria-label="Happy!">
      <span style="color:var(--orange)">H</span><span style="color:var(--pink)">a</span><span style="color:var(--purple)">p</span><span style="color:var(--blue)">p</span><span style="color:var(--green)">y</span><span style="color:var(--pink)">!</span>
    </p>

    <ul class="values">
      <li class="value"><span class="value__label">社会の</span>
        <span class="value__word"><span class="tile" style="background:var(--sky)">H</span><span class="tile" style="background:var(--peach)">a</span><span class="tile" style="background:var(--rose)">p</span><span class="tile" style="background:var(--mauve)">p</span><span class="tile" style="background:var(--pink)">y</span></span>
        <span class="value__bang" style="color:var(--pink)">!</span></li>
      <li class="value"><span class="value__label">顧客の</span>
        <span class="value__word"><span class="tile" style="background:var(--blue)">H</span><span class="tile" style="background:var(--purple)">a</span><span class="tile" style="background:var(--pink)">p</span><span class="tile" style="background:var(--lilac)">p</span><span class="tile" style="background:var(--grey)">y</span></span>
        <span class="value__bang" style="color:var(--orange)">!</span></li>
      <li class="value"><span class="value__label">仲間の</span>
        <span class="value__word"><span class="tile" style="background:var(--mauve)">H</span><span class="tile" style="background:var(--rose)">a</span><span class="tile" style="background:var(--mint)">p</span><span class="tile" style="background:var(--purple)">p</span><span class="tile" style="background:var(--pink)">y</span></span>
        <span class="value__bang" style="color:var(--purple)">!</span></li>
      <li class="value"><span class="value__label">家族の</span>
        <span class="value__word"><span class="tile" style="background:var(--peach)">H</span><span class="tile" style="background:var(--orange)">a</span><span class="tile" style="background:var(--green)">p</span><span class="tile" style="background:var(--rose)">p</span><span class="tile" style="background:var(--grey)">y</span></span>
        <span class="value__bang" style="color:var(--green)">!</span></li>
      <li class="value"><span class="value__label">自分の</span>
        <span class="value__word"><span class="tile" style="background:var(--lilac)">H</span><span class="tile" style="background:var(--mint)">a</span><span class="tile" style="background:var(--rose)">p</span><span class="tile" style="background:var(--yellow)">p</span><span class="tile" style="background:var(--mint)">y</span></span>
        <span class="value__bang" style="color:var(--pink)">!</span></li>
    </ul>

    <p class="brand">LUMINA</p>

    <div class="ornament ornament--left" role="img" aria-label="pink flower ornament in the corner"></div>
    <div class="ornament ornament--right" role="img" aria-label="soft brown swirl ornament along the bottom"></div>
  </div>
</main>
</body>
</html>
```